Postcard Design

We provide humorous speechwriting and presentation coaching services, primarily for the wedding market (best man, father of the bride, maid of honor). We'd like a design that incoporates the blue and white logo colors into a nice overall design, with the pitch:
"Use the power of humor to deliver the BEST speech of your life!"
Target Market(s)
Wedding market (best man, bride/groom)
Industry/Entity Type
Wedding
Requirements
Must have
- Bulletpoints for services provided:
- Speechwriting
- Presentation Coaching
- Emcee & Officiant Services
Listing of benefits provided:
- Conquer stage fright
- Deliver your speech like a pro
- Be funny AND tactful
- Leave them wanting more
Contact info -
Derek Hanslow
Derek@JollyQuill.com
www.JollyQuill.com
Testimonial quotes:
"People are STILL raving about that speech at our wedding. Thanks Jolly Quill!"
- Karen & Paul Dessaro, Baltimore, MD
"With the help of Jolly Quill, my best man speech brought down the house!"
- Trent Galloway, Melville, NY

```html
<!DOCTYPE html>
<html lang="en">
<head>
<meta charset="utf-8">
<title>Jolly Quill Postcard</title>
<link rel="stylesheet" href="https://fonts.googleapis.com/css2?family=Oswald:wght@500;600&family=Open+Sans:wght@400;600;700&display=swap">
<style>
:root{
  --navy:#1b2466;
  --navy-deep:#0d1240;
  --navy-light:#2c3a8f;
  --white:#ffffff;
  --paper:#f2f2f2;
  --line:#b9bccc;
  --ink:#1b2466;
  --photo-a:#e9e6e2;
  --photo-b:#1a1a1f;
}
*{box-sizing:border-box;margin:0;padding:0}
html,body{width:1200px;height:900px;overflow:hidden;background:var(--paper)}
body{font-family:"Open Sans",Arial,sans-serif;position:relative}
.card{position:absolute;width:600px;height:400px;background:var(--white);overflow:hidden;box-shadow:0 2px 10px rgba(0,0,0,.12)}
.card--front{left:300px;top:40px}
.card--back{left:300px;top:465px}

/* brand */
.brand{display:flex;align-items:center;gap:7px;position:absolute;z-index:2}
.brand__dot{width:14px;height:14px;border-radius:50%;background:var(--navy)}
.brand__name{font-family:"Open Sans",Arial,sans-serif;font-weight:700;font-size:15px;color:var(--navy);text-transform:uppercase;letter-spacing:.5px;white-space:nowrap}

/* front */
.front__photo{position:absolute;left:30px;top:70px;width:290px;height:330px;
  background:linear-gradient(180deg,var(--photo-a) 0%,var(--photo-a) 20%,#3a3a44 45%,var(--photo-b) 100%)}
.front__panel{position:absolute;inset:0;
  background:linear-gradient(160deg,var(--navy-light),var(--navy) 45%,var(--navy-deep));
  clip-path:polygon(40% 4%,100% 4%,100% 100%,66% 100%)}
.front__brand{left:22px;top:30px}
.pitch{position:absolute;right:26px;top:28px;width:300px;text-align:right;color:var(--white);font-weight:normal}
.pitch__line{display:block}
.pitch__small{font-family:"Oswald",sans-serif;font-weight:500;font-size:22px;letter-spacing:1px;line-height:1.1}
.pitch__big{font-family:"Oswald",sans-serif;font-weight:600;font-size:50px;line-height:1;letter-spacing:.5px}
.pitch__mid{font-family:"Oswald",sans-serif;font-weight:600;font-size:32px;line-height:1;letter-spacing:.5px}
.benefits{position:absolute;right:26px;top:272px;text-align:right;color:var(--white);list-style:none}
.benefits li{line-height:1.25}
.benefits .lead{font-weight:700;font-size:15px}
.benefits .sub{font-size:12px}
.front__web{position:absolute;right:0;bottom:0;width:170px;height:26px;background:var(--navy-deep);
  color:var(--white);font-size:11px;text-align:right;padding:6px 20px 0 0}

/* back */
.back__panel{position:absolute;inset:0;
  background:linear-gradient(200deg,var(--navy-light),var(--navy) 40%,var(--navy-deep));
  clip-path:polygon(0 29%,60% 17%,60% 100%,0 100%)}
.back__brand{left:190px;top:26px}
.back__info{position:absolute;left:26px;top:128px;width:320px;color:var(--white)}
.contact__name{font-weight:700;font-size:14px}
.contact__line{font-size:12px;line-height:1.35}
.section-title{font-family:"Oswald",sans-serif;font-weight:500;font-size:19px;text-transform:uppercase;margin-top:8px;line-height:1.2}
.services{list-style:none;font-size:16px;line-height:1.25}
.quote{font-size:10.5px;line-height:1.3;margin-top:4px}
.quote cite{display:block;font-style:normal;font-size:9px;opacity:.85}
.stamp{position:absolute;right:30px;top:24px;width:110px;height:90px;border:1px solid var(--line);
  font-size:9px;color:var(--ink);text-align:center;padding-top:10px}
.address{position:absolute;right:30px;top:150px;width:210px;list-style:none}
.address li{height:42px;border-bottom:1px solid var(--line)}
</style>
</head>
<body>

<section class="card card--front" aria-label="Postcard front">
  <div class="front__photo" role="img" aria-label="Photo of a man in a tuxedo raising a champagne glass while reading a speech card"></div>
  <div class="front__panel"></div>
  <div class="brand front__brand"><span class="brand__dot"></span><span class="brand__name">Jolly Quill</span></div>
  <h1 class="pitch">
    <span class="pitch__line pitch__small">Use the power of</span>
    <span class="pitch__line pitch__big">HUMOR</span>
    <span class="pitch__line pitch__small">to deliver the</span>
    <span class="pitch__line pitch__mid">BEST</span>
    <span class="pitch__line pitch__big">SPEECH</span>
    <span class="pitch__line pitch__small">of your life</span>
  </h1>
  <ul class="benefits">
    <li class="lead">Conquer stage fright</li>
    <li class="sub">Deliver your speech like a pro</li>
    <li class="lead">Be funny &amp; tactful</li>
    <li class="sub">Leave them wanting more</li>
  </ul>
  <div class="front__web">www.JollyQuill.com</div>
</section>

<section class="card card--back" aria-label="Postcard back">
  <div class="back__panel"></div>
  <div class="brand back__brand"><span class="brand__dot"></span><span class="brand__name">Jolly Quill</span></div>
  <div class="back__info">
    <p class="contact__name">Derek Hanslow</p>
    <p class="contact__line">Derek@JollyQuill.com</p>
    <p class="contact__line">www.JollyQuill.com</p>
    <h2 class="section-title">Our Services</h2>
    <ul class="services">
      <li>Speechwriting</li>
      <li>Presentation Coaching</li>
      <li>Emcee &amp; Officiant Services</li>
    </ul>
    <h2 class="section-title">What People Say</h2>
    <blockquote class="quote">“People are STILL raving about that speech at our wedding. Thanks Jolly Quill!”
      <cite>– Karen &amp; Paul Dessaro, Baltimore, MD</cite></blockquote>
    <blockquote class="quote">“With the help of Jolly Quill, my best man speech brought down the house!”
      <cite>– Trent Galloway, Melville, NY</cite></blockquote>
  </div>
  <div class="stamp">stamp here</div>
  <ul class="address"><li></li><li></li><li></li><li></li><li></li></ul>
</section>

</body>
</html>
```